Business Card Design and Basic Text Logo

We are looking for a business card design for an e-business company. Our business is the parent company of a few website businesses. The final logo and business card design will communicate a conservative but modern and expansive business

The Logo text is: 57Commerce
We would also like a basic text logo design for 57Commerce. The logo could also fill up the reverse side of the business card.

The colours we would like to use are:
White
Navy
Black

This is the text that will be added to the card:

Dean Calloway
Business Development Manager

Phone: +61 417 586 924
Email: dean.calloway@57commerce.com.au

Industry/Entity Type

Business

Logo Text

57Commerce

Logo styles of interest
Pictorial/Combination Logo
Requirements
Must have
• Modern and attractive design
Nice to have
• communicate a conservative but modern and expansive business
Should not have
• Should be too dull and plan
• But also should be overly colourful

```html
<!DOCTYPE html>
<html lang="en">
<head>
<meta charset="utf-8">
<title>57Commerce Business Card</title>
<link rel="stylesheet" href="https://fonts.googleapis.com/css2?family=Arimo:wght@400;700&display=swap">
<style>
  :root {
    --page-bg: #ffffff;
    --card-black: #050608;
    --navy-glow: #1d4f96;
    --navy-deep: #0c1f3f;
    --accent-blue: #2f6fc4;
    --text-white: #ffffff;
    --text-soft: #e6e9ee;
  }
  * { box-sizing: border-box; margin: 0; padding: 0; }
  html, body {
    width: 1200px;
    height: 900px;
    overflow: hidden;
    background: var(--page-bg);
    font-family: "Arimo", Arial, sans-serif;
  }
  .canvas {
    position: relative;
    width: 1200px;
    height: 900px;
  }
  .card {
    position: absolute;
    top: 300px;
    width: 525px;
    height: 300px;
    border-radius: 22px;
    background: var(--card-black);
    overflow: hidden;
    box-shadow: 0 14px 30px rgba(0,0,0,0.18);
  }
  .card--front { left: 50px; }
  .card--back { left: 625px; }

  .dot-field {
    position: absolute;
    left: 0;
    width: 100%;
  }
  .dot-field--top {
    top: 0;
    height: 150px;
    background: linear-gradient(180deg, var(--navy-deep) 0%, var(--navy-glow) 30%, rgba(29,79,150,0.35) 70%, rgba(5,6,8,0) 100%);
  }
  .dot-field--bottom {
    bottom: 0;
    height: 120px;
    background: linear-gradient(0deg, var(--navy-deep) 0%, var(--navy-glow) 25%, rgba(29,79,150,0.3) 65%, rgba(5,6,8,0) 100%);
  }

  .wordmark {
    position: absolute;
    left: 0;
    width: 100%;
    text-align: center;
    color: var(--text-white);
    font-weight: 700;
    letter-spacing: 0.5px;
  }
  .card--front .wordmark { top: 92px; font-size: 42px; }
  .card--back .wordmark { top: 118px; font-size: 58px; }

  .contact {
    position: absolute;
    left: 28px;
    top: 168px;
  }
  .contact__name {
    color: var(--accent-blue);
    font-size: 16px;
    font-weight: 400;
  }
  .contact__role {
    color: var(--text-soft);
    font-size: 11px;
    margin-top: 3px;
  }
  .contact__list {
    list-style: none;
    margin-top: 16px;
  }
  .contact__item {
    display: flex;
    align-items: center;
    gap: 7px;
    color: var(--text-white);
    font-size: 16px;
    line-height: 21px;
  }
  .contact__icon {
    width: 16px;
    height: 16px;
    flex: none;
  }
</style>
</head>
<body>
<main class="canvas">

  <section class="card card--front" aria-label="Card front">
    <div class="dot-field dot-field--top" role="img" aria-label="Blue perspective dot pattern fading into black"></div>
    <div class="wordmark">57Commerce</div>
    <div class="contact">
      <p class="contact__name">Dean Calloway</p>
      <p class="contact__role">Business Development Manager</p>
      <ul class="contact__list">
        <li class="contact__item">
          <svg class="contact__icon" viewBox="0 0 24 24" aria-hidden="true">
            <path fill="#2f6fc4" d="M6.6 10.8c1.4 2.8 3.8 5.1 6.6 6.6l2.2-2.2c.3-.3.7-.4 1-.2 1.1.4 2.3.6 3.6.6.6 0 1 .4 1 1V20c0 .6-.4 1-1 1C10.6 21 3 13.4 3 4c0-.6.4-1 1-1h3.5c.6 0 1 .4 1 1 0 1.3.2 2.5.6 3.6.1.3 0 .7-.2 1L6.6 10.8z"/>
          </svg>
          <span>+61 417 586 924</span>
        </li>
        <li class="contact__item">
          <svg class="contact__icon" viewBox="0 0 24 24" aria-hidden="true">
            <rect x="2" y="5" width="20" height="14" rx="2" fill="#2f6fc4"/>
            <path d="M3 6.5l9 6.5 9-6.5" fill="none" stroke="#ffffff" stroke-width="1.6"/>
          </svg>
          <span>dean.calloway@57commerce.com.au</span>
        </li>
      </ul>
    </div>
  </section>

  <section class="card card--back" aria-label="Card back">
    <div class="dot-field dot-field--top" role="img" aria-label="Blue perspective dot pattern along the top edge"></div>
    <div class="dot-field dot-field--bottom" role="img" aria-label="Blue perspective dot pattern along the bottom edge"></div>
    <div class="wordmark">57Commerce</div>
  </section>

</main>
</body>
</html>
```